Logo für Trockenbauarbeiten aller Art, Spachtelarbeiten und Verputzarbeiten
Zielgruppe
Gegenstand des Unternehmens ist Trockenbauarbeiten aller Art, Spachtelarbeiten und Verputzarbeiten.
Unsere Zielgruppe sind Menschen ab 30 Jahren aufwärts, wir interessieren uns für den einzelnen Hausbesitzer oder Eigentumswohnungbesitzer. Wir benötigen einen hohen Wiedererkennungseffekt.
Wir benötigen Designvorlagen für eine Facebook Seite, Instagram und werden über diese beiden Plattformen auch Werbung schalten, daher benötigen wir dafür auch die verschiedenen Designvorlagen, um verschiedenen Werbekampangen zu erstellen.
Name des Unternehmens: 'WAND-PLAN KOLLHAGEN GmbH'
Aufgabenstellung
Wichtig ist bei den verschiedenen Designs, dass wir Leads bzw. Kundenaufträge sammeln können. Wir müssen herausstechen aus der Masse an Handwerkern. Wir sind die absoluten Spezialisten in unserem Gebiet. Des Weiteren werden wir aus den Materialen diverse Kampagnen erstellen die das komplette Jahr 2022 durchlaufen werden. Vorzugsweise werden wir hierfür die Plattfirm Facebook verwenden, aber auch andere Kanäle.
WICHTIG: Das Logo mit dem roten Haus ist unser original Logo!

```html
<!DOCTYPE html>
<html lang="de">
<head>
<meta charset="utf-8">
<title>WAND-PLAN KOLLHAGEN – Social Post</title>
<link rel="stylesheet" href="https://fonts.googleapis.com/css2?family=Montserrat:wght@700;800&family=Open+Sans:wght@400;600;700&display=swap">
<style>
  :root {
    --frame-dark: #282628;
    --house-dark: #332f2e;
    --brand-red: #f20000;
    --ink: #231f20;
    --ink-soft: #333333;
    --paper: #ffffff;
    --photo-light: #dcdad6;
    --photo-mid: #a9a29a;
    --photo-warm: #7d6650;
    --pattern-tone: rgba(35, 31, 32, 0.14);
  }
  html, body {
    margin: 0;
    padding: 0;
    width: 1200px;
    height: 1200px;
    overflow: hidden;
    background: var(--frame-dark);
  }
  .post {
    position: relative;
    width: 1200px;
    height: 1200px;
    background: var(--frame-dark);
    font-family: "Open Sans", sans-serif;
    color: var(--ink);
  }
  .card-shapes {
    position: absolute;
    inset: 0;
  }
  .brand {
    position: absolute;
    left: 152px;
    top: 196px;
    display: flex;
    align-items: center;
    gap: 16px;
  }
  .brand-mark {
    width: 26px;
    height: 26px;
    background: var(--brand-red);
  }
  .brand-name {
    font-family: "Montserrat", sans-serif;
    font-weight: 800;
    font-size: 44px;
    line-height: 48px;
    color: var(--ink);
  }
  .headline {
    position: absolute;
    left: 156px;
    top: 332px;
    margin: 0;
    font-family: "Montserrat", sans-serif;
    font-weight: 800;
    font-size: 58px;
    line-height: 71px;
    color: var(--ink);
  }
  .headline .accent { color: var(--brand-red); }
  .headline-rule {
    position: absolute;
    left: 158px;
    top: 571px;
    width: 125px;
    height: 6px;
    background: var(--brand-red);
  }
  .intro {
    position: absolute;
    left: 157px;
    top: 601px;
    margin: 0;
    font-size: 22px;
    line-height: 34px;
    color: var(--ink);
    white-space: nowrap;
  }
  .service-title {
    position: absolute;
    left: 156px;
    top: 740px;
    margin: 0;
    font-family: "Montserrat", sans-serif;
    font-weight: 800;
    font-size: 43px;
    line-height: 56px;
    color: var(--brand-red);
  }
  .service-list {
    position: absolute;
    left: 163px;
    top: 807px;
    margin: 0;
    padding: 0 0 0 23px;
    width: 340px;
    font-size: 21px;
    line-height: 31px;
    color: var(--ink-soft);
  }
  .service-list li { margin-bottom: 3px; }
  .service-list li::marker { color: var(--ink-soft); font-size: 18px; }
  .social {
    position: absolute;
    left: 151px;
    top: 1015px;
    display: flex;
    align-items: center;
    gap: 80px;
  }
  .social-dot {
    width: 44px;
    height: 44px;
    border-radius: 50%;
    background: var(--brand-red);
  }
  .social-handle {
    font-weight: 700;
    font-size: 28px;
    color: var(--ink-soft);
  }
  .contact {
    position: absolute;
    left: 740px;
    top: 1012px;
    display: flex;
    align-items: center;
    gap: 18px;
    color: var(--paper);
  }
  .contact svg { width: 50px; height: 50px; }
  .contact-number {
    font-weight: 700;
    font-size: 38px;
    line-height: 50px;
    color: var(--paper);
  }
</style>
</head>
<body>
<main class="post">
  <svg class="card-shapes" width="1200" height="1200" viewBox="0 0 1200 1200">
    <rect class="card" x="104" y="104" width="1017" height="992" fill="var(--paper)"/>
    <polygon class="red-field" points="787,104 1121,104 1121,1096 612,1096" fill="var(--brand-red)"/>
    <rect class="pattern-area" role="img" aria-label="Dekoratives Punktraster" x="634" y="143" width="188" height="38" rx="4" fill="var(--pattern-tone)"/>
    <path class="house-frame" d="M561,413 L966,134 L1121,242 L1121,848 Q820,862 561,994 Z" fill="var(--house-dark)"/>
    <defs>
      <linearGradient id="photoTone" x1="0" y1="0" x2="1" y2="0.3">
        <stop offset="0" stop-color="var(--photo-warm)"/>
        <stop offset="0.3" stop-color="var(--photo-mid)"/>
        <stop offset="0.6" stop-color="var(--photo-light)"/>
        <stop offset="1" stop-color="#ececea"/>
      </linearGradient>
    </defs>
    <path class="house-photo" role="img" aria-label="Foto: Handwerker auf einer Leiter montiert Gipskartonplatten an einer gedämmten Trockenbauwand" d="M589,427 L961,178 L1121,289 L1121,830 Q830,842 589,939 Z" fill="url(#photoTone)"/>
  </svg>

  <div class="brand">
    <span class="brand-mark"></span>
    <span class="brand-name">WAND-PLAN<br>KOLLHAGEN</span>
  </div>

  <h1 class="headline">Lorem<br><span class="accent">Ipsum dolor</span><br>sit amet</h1>
  <div class="headline-rule"></div>

  <p class="intro">consectetur adipiscing elit, sed do<br>eiusmod tempor incididunt ut<br>labore et dolore magna aliqua.</p>

  <h2 class="service-title">Our Service</h2>
  <ul class="service-list">
    <li>Lorem ipsum dolor sit amet</li>
    <li>Lorem ipsum dolor sit amet consectetur adipiscing elit</li>
    <li>Lorem ipsum dolor sit amet</li>
    <li>Lorem ipsum dolor sit amet</li>
  </ul>

  <div class="social">
    <span class="social-dot"></span>
    <span class="social-handle">Wand_plan_kollhagen</span>
  </div>

  <div class="contact">
    <svg viewBox="0 0 50 50" aria-hidden="true">
      <path d="M12 8 C9 9 6 12 6 16 C7 28 20 42 33 44 C37 44 40 41 41 38 L34 31 C33 30 31 30 30 31 L27 34 C21 31 17 26 15 21 L18 18 C19 17 19 15 18 14 Z" fill="var(--paper)"/>
      <path d="M28 12 A10 10 0 0 1 38 22 M30 5 A17 17 0 0 1 45 20" fill="none" stroke="var(--paper)" stroke-width="2.5" stroke-linecap="round"/>
    </svg>
    <span class="contact-number">0160/4817325</span>
  </div>
</main>
</body>
</html>
```